Web Design Project for DJ

We need a web design for a DJ. Our client is a freelance DJ who already has a regular gig at a major night club but is looking to expand his exposure. He is located in a major metropolitan area and is looking for further gigs. He is hoping to generate further business via the website, including bookings via the site.

For reference his pagelinker page is here https://www.pagelinker.example/pages/DJ-Vorn/730162948415207

Following face to face discussions with the client today we have made a few small alterations to the brief.  We are hoping to have some images uploaded shortly.

Target Market(s)

Event planners, night club owners, radio stations, younger age groups (16-35)

Industry/Entity Type

Business

Requirements
Must have
• Name is DJVorn, this should obviously feature prominently. His current business card is attached as an example.

Links to Pagelinker and Tunedrift

Cool, modern look, slightly edgy.

Site will be built in Joomla, so a front page and secondary page template is required.
Nice to have
• Blog style layout to front page featuring recent and upcoming gigs.

Secondary pages may include a more expansive blog, a list of upcoming gigs, and a booking form.

Darker colour palettes preferred and use of same/similar fonts to those on the business card are an obvious plus

```html
<!DOCTYPE html>
<html lang="en">
<head>
<meta charset="utf-8">
<title>DJVorn – Book Now</title>
<link rel="stylesheet" href="https://fonts.googleapis.com/css2?family=Play:wght@400;700&display=swap">
<style>
  :root {
    --bg: #121212;
    --bg-glow: #2e2e2e;
    --panel-line: #3a3a3a;
    --tab-bg: #2f2f2f;
    --text: #e6e6e6;
    --muted: #9a9a9a;
    --accent: #5aa8ff;
    --accent-dim: #3d6fb0;
    --field-line: #8a8a8a;
    --field-bg: #161616;
    --row-line: #222;
  }
  * { box-sizing: border-box; margin: 0; padding: 0; }
  html, body { width: 694px; height: 1200px; overflow: hidden; }
  body {
    position: relative;
    background: radial-gradient(ellipse 420px 260px at 330px 40px, var(--bg-glow), var(--bg) 75%), var(--bg);
    font-family: "Play", sans-serif;
    color: var(--text);
  }
  .site-name {
    position: absolute; left: 50px; top: 31px;
    font-family: "Play", sans-serif; font-weight: 700;
    font-size: 34px; line-height: 40px; color: var(--text);
  }
  .main-nav { position: absolute; top: 45px; left: 400px; display: flex; gap: 22px; font-size: 10.5px; letter-spacing: .5px; }
  .main-nav a { color: var(--text); text-decoration: none; }
  .main-nav a.is-active { color: var(--accent); font-weight: 700; }

  .hero { position: absolute; left: 50px; top: 94px; width: 594px; height: 222px; }
  .hero-image {
    position: absolute; inset: 0;
    background: linear-gradient(180deg, #0a1d5a 0%, #1540b8 40%, #0d2a80 70%, #071338 100%);
  }
  .hero svg { position: absolute; inset: 0; }

  .section-title {
    position: absolute; font-weight: 700; font-size: 11.5px; letter-spacing: 1px;
    display: flex; align-items: center; gap: 9px;
  }
  .section-title::before {
    content: ""; border-left: 5px solid var(--text);
    border-top: 3px solid transparent; border-bottom: 3px solid transparent;
  }
  .booking-title { left: 50px; top: 353px; }
  .booking-rule { position: absolute; left: 50px; top: 374px; width: 341px; height: 1px; background: var(--accent-dim); }

  .fieldset { position: absolute; left: 50px; width: 296px; border: 1px solid var(--panel-line); }
  .legend {
    position: absolute; left: 6px; top: -10px; width: 95px; height: 17px;
    background: var(--tab-bg); color: var(--accent); font-size: 11px; padding: 1px 0 0 7px;
  }
  .field { position: absolute; left: 13px; width: 228px; display: flex; align-items: center; justify-content: space-between; }
  .field label { font-size: 7.8px; color: var(--muted); line-height: 11px; width: 100px; }
  .field input { width: 89px; height: 15px; border: 1px solid var(--field-line); background: var(--field-bg); }

  .send-button {
    position: absolute; left: 50px; top: 1067px; width: 79px; height: 23px;
    border: 1px solid var(--accent-dim); background: transparent; color: var(--accent);
    font-family: "Play", sans-serif; font-size: 9.5px; letter-spacing: .5px;
  }

  .gigs { position: absolute; left: 454px; top: 345px; width: 190px; height: 326px; border: 1px solid var(--panel-line); }
  .gigs .section-title { left: 12px; top: 9px; }
  .gigs-rule { position: absolute; left: 0; right: 0; top: 30px; height: 1px; background: var(--panel-line); }
  .gigs table { position: absolute; left: 13px; top: 43px; width: 134px; border-collapse: collapse; font-size: 7.3px; }
  .gigs th { color: var(--accent); font-weight: 400; text-align: left; height: 18px; padding-left: 4px; }
  .gigs td { height: 25.3px; border-bottom: 1px solid var(--row-line); padding-left: 4px; color: var(--text); }
  .gigs tr:last-child td { border-bottom: none; }
  .gigs .col-date { width: 57px; }

  .site-footer { position: absolute; left: 102px; top: 1158px; width: 491px; border-top: 1px solid var(--accent-dim); text-align: center; font-size: 8px; color: var(--muted); padding-top: 9px; }
</style>
</head>
<body>
  <header>
    <div class="site-name">DJVorn</div>
    <nav class="main-nav">
      <a href="#">GIGS.</a><a href="#">PHOTOS.</a><a href="#">CONTACT.</a><a href="#" class="is-active">BOOK NOW.</a>
    </nav>
  </header>

  <section class="hero">
    <div class="hero-image" role="img" aria-label="Festival main stage lit in blue with a large crowd"></div>
    <svg width="594" height="222" viewBox="0 0 594 222">
      <polygon points="0,0 96,0 0,96" fill="#1c1c1c" stroke="#333"/>
      <polygon points="594,222 496,222 594,124" fill="#1c1c1c" stroke="#333"/>
      <polyline points="20,46 20,20 48,20" fill="none" stroke="#d0d0d0" stroke-width="2"/>
      <polyline points="574,176 574,202 546,202" fill="none" stroke="#5aa8ff" stroke-width="2"/>
      <rect x="0.5" y="0.5" width="593" height="221" fill="none" stroke="#2a2a2a"/>
    </svg>
  </section>

  <main>
    <h2 class="section-title booking-title">BOOKING FORM</h2>
    <div class="booking-rule"></div>

    <form>
      <div class="fieldset" style="top:404px;height:207px">
        <div class="legend">Event details</div>
        <div class="field" style="top:27px"><label>Date of show</label><input></div>
        <div class="field" style="top:52px"><label>Proposed set time</label><input></div>
        <div class="field" style="top:78px"><label>Door charge</label><input></div>
        <div class="field" style="top:103px"><label>Offer amount</label><input></div>
        <div class="field" style="top:134px"><label>Which DJs have you booked previously?</label><input></div>
        <div class="field" style="top:171px"><label>Who else is booked for the event?</label><input></div>
      </div>

      <div class="fieldset" style="top:638px;height:241px">
        <div class="legend">Venue details</div>
        <div class="field" style="top:27px"><label>Venue name</label><input></div>
        <div class="field" style="top:52px"><label>Name of club night</label><input></div>
        <div class="field" style="top:78px"><label>Venue capacity</label><input></div>
        <div class="field" style="top:103px"><label>Country</label><input></div>
        <div class="field" style="top:128px"><label>City</label><input></div>
        <div class="field" style="top:154px"><label>State/Province</label><input></div>
        <div class="field" style="top:179px"><label>Street address</label><input></div>
        <div class="field" style="top:204px"><label>Postcode</label><input></div>
      </div>

      <div class="fieldset" style="top:905px;height:143px">
        <div class="legend">Your details</div>
        <div class="field" style="top:27px"><label>First name</label><input></div>
        <div class="field" style="top:52px"><label>Last name</label><input></div>
        <div class="field" style="top:77px"><label>Contact number</label><input></div>
        <div class="field" style="top:102px"><label>Email</label><input></div>
      </div>

      <button class="send-button" type="button">SEND FORM</button>
    </form>
  </main>

  <aside class="gigs">
    <h2 class="section-title">UPCOMING GIGS</h2>
    <div class="gigs-rule"></div>
    <table>
      <thead><tr><th class="col-date">Date</th><th>Venue</th></tr></thead>
      <tbody>
        <tr><td>01 Jan</td><td>Venue name nr.1</td></tr>
        <tr><td>02 Feb</td><td>Venue name nr.2</td></tr>
        <tr><td>03 Mar</td><td>Venue name nr.3</td></tr>
        <tr><td>04 Apr</td><td>Venue name nr.4</td></tr>
        <tr><td>05 May</td><td>Venue name nr.5</td></tr>
        <tr><td>06 Jun</td><td>Venue name nr.6</td></tr>
        <tr><td>07 Jul</td><td>Venue name nr.7</td></tr>
        <tr><td>08 Aug</td><td>Venue name nr.8</td></tr>
        <tr><td>09 Sep</td><td>Venue name nr.9</td></tr>
        <tr><td>10 Oct</td><td>Venue name nr.10</td></tr>
      </tbody>
    </table>
  </aside>

  <footer class="site-footer">© Copyright DjVorn 2013. All rights reserved.</footer>
</body>
</html>
```